Guava Energy Bar Logo and Packaging Art for New Brand/Product

I want to design product packaging for a Guava energy bar that is made primarily from the guava fruit grown on Hawaii. It is a high energy bar designed for quick energy for athletes, hikers, cyclists and adventurers. I want to play in the P.A.E.R and call the bar the "Papaya (prime) Above Every Rival." It will be made from real Guava and wrapped in a compostable leaf wrapper, gluten free and vegan friendly. I want to play on the fact that Guava is a superfood packed with essential vitamins and minerals and free from artificial colours and preservatives.
Target Market(s)
Athletes, Hikers, Cyclists, Runners, Climbers, Triathletes and Adventurers
Requirements
Must have
- I want to make the P.A.E.R. (prime above every rival) woven in the brand and logo with a strong reference to Guava; the super fruit!
Nice to have
- Take a look at the brand and packaging for Tundra Bars

```html
<!DOCTYPE html>
<html lang="en">
<head>
<meta charset="utf-8">
<title>Papaya (prime) Above Every Rival – Energy Bar Pack</title>
<link rel="stylesheet" href="https://fonts.googleapis.com/css2?family=Archivo:wght@700&family=Oswald:wght@700&family=Stardos+Stencil:wght@700&display=swap">
<style>
  :root {
    --ink: #2c1a2c;
    --orange: #fbb03b;
    --cream: #fbf6c0;
    --pale-yellow: #f8f19a;
    --stencil-yellow: #f4ee5a;
    --leaf-green: #1e5c3c;
    --lime: #f5f25a;
    --guava-light: #b6e28a;
    --guava-mid: #8fcf5e;
    --guava-dark: #3f7a2e;
    --badge-brown: #6b4a22;
    --badge-green: #3aa83a;
    --white: #ffffff;
  }
  html, body {
    margin: 0;
    padding: 0;
    width: 773px;
    height: 1200px;
    overflow: hidden;
    background: var(--white);
  }
  .pack {
    display: block;
    width: 773px;
    height: 1200px;
  }
  .label-sans { font-family: "Archivo", Arial, sans-serif; font-weight: 700; }
  .banner-type { font-family: "Oswald", Impact, sans-serif; font-weight: 700; }
  .stencil-type { font-family: "Stardos Stencil", "Courier New", serif; font-weight: 700; }
</style>
</head>
<body>
<svg class="pack" viewBox="0 0 732 1137" preserveAspectRatio="none" xmlns="http://www.w3.org/2000/svg">
  <!-- fruit photo field -->
  <rect class="fruit-photo" role="img" aria-label="Close-up photograph of a pile of fresh green guava fruit"
        x="6" y="480" width="720" height="440" fill="url(#guavaPhoto)"/>
  <defs>
    <radialGradient id="guavaPhoto" cx="0.55" cy="0.45" r="0.75">
      <stop offset="0" stop-color="var(--guava-light)"/>
      <stop offset="0.6" stop-color="var(--guava-mid)"/>
      <stop offset="1" stop-color="var(--guava-dark)"/>
    </radialGradient>
    <linearGradient id="guavaArt" x1="0" y1="0" x2="1" y2="1">
      <stop offset="0" stop-color="#d9e84a"/>
      <stop offset="0.5" stop-color="#3f8a3a"/>
      <stop offset="1" stop-color="#1e5c3c"/>
    </linearGradient>
  </defs>

  <!-- top bands -->
  <rect class="top-band" x="15" y="15" width="705" height="58" fill="var(--orange)"/>
  <rect class="title-band" x="15" y="70" width="705" height="75" fill="var(--ink)"/>
  <text class="label-sans" x="367" y="122" text-anchor="middle" font-size="30" fill="var(--pale-yellow)">GUAVA ENERGY BAR</text>

  <!-- orange headline panel -->
  <path class="headline-panel" d="M4 145 L4 488 Q4 500 20 503 Q366 560 712 503 Q728 500 728 488 L728 145 Z"
        fill="var(--orange)" stroke="var(--ink)" stroke-width="8"/>
  <text class="stencil-type" x="366" y="268" text-anchor="middle" font-size="128" textLength="690" lengthAdjust="spacingAndGlyphs" fill="var(--stencil-yellow)">PRIME ABOVE</text>
  <text class="stencil-type" x="366" y="392" text-anchor="middle" font-size="128" textLength="690" lengthAdjust="spacingAndGlyphs" fill="var(--stencil-yellow)">EVERY RIVAL</text>

  <!-- brand name -->
  <text class="banner-type" x="382" y="432" text-anchor="middle" font-size="52" fill="var(--ink)">P.A.E.R</text>

  <!-- guava illustration -->
  <ellipse class="guava-illustration" role="img" aria-label="Illustrated striped green guava fruit with stem and leaf"
           cx="205" cy="690" rx="165" ry="165" fill="url(#guavaArt)" stroke="var(--ink)" stroke-width="6"/>

  <!-- headline banner -->
  <path class="banner-top" d="M190 732 L555 732 L585 772 L555 812 L190 812 L158 772 Z"
        fill="var(--leaf-green)" stroke="var(--ink)" stroke-width="8"/>
  <text class="banner-type" x="372" y="800" text-anchor="middle" font-size="62" textLength="330" lengthAdjust="spacingAndGlyphs" fill="var(--cream)">PRIME ABOVE</text>
  <path class="banner-bottom" d="M222 815 L548 815 L575 860 L548 905 L222 905 L195 860 Z"
        fill="var(--lime)" stroke="var(--ink)" stroke-width="8"/>
  <text class="banner-type" x="385" y="884" text-anchor="middle" font-size="56" textLength="310" lengthAdjust="spacingAndGlyphs" fill="var(--leaf-green)">EVERY RIVAL</text>

  <!-- claims strip -->
  <rect class="claims-strip" x="6" y="915" width="720" height="152" fill="var(--cream)"/>
  <circle class="claim-badge" cx="106" cy="992" r="62" fill="var(--badge-brown)"/>
  <circle class="claim-badge" cx="638" cy="992" r="60" fill="var(--badge-green)"/>

  <!-- footer band -->
  <rect class="footer-band" x="6" y="1065" width="720" height="72" fill="var(--ink)"/>
  <text class="label-sans" x="366" y="1110" text-anchor="middle" font-size="30" fill="var(--pale-yellow)">SUPER FRUIT</text>
</svg>
</body>
</html>
```